Kalm to Bloom: Prespective and Balence in People's Lives Needs a Buissness Card Design

Calm to Bloom Community Center is an organization that seeks to bring balance into people's lives. Main services include: guided meditation, group brainstorming, and guided counseling. Calm to Bloom combines Eastern practices, i.e. Buddhism, Hinduism, and Taoism, with Western practices: therapy, group brainstorming and healing. We would like a double sided card: 1) front vertical with image, 2) back horizontal with information. The main colors for the card are red, white, black. Different finishes would be nice--please no high gloss. Matte, pearlized, embossing--used tactfully and sparingly would be nice. The card should convey balance/harmony in a modern world.

```html
<!DOCTYPE html>
<html lang="en">
<head>
<meta charset="utf-8">
<title>Calm to Bloom Community Center – Business Card</title>
<link rel="stylesheet" href="https://fonts.googleapis.com/css2?family=Francois+One&family=Exo+2:wght@400;500&display=swap">
<style>
  :root {
    --page-bg: #1f1f1f;
    --card-dark: #2c2c2c;
    --card-black: #111111;
    --paper-white: #ffffff;
    --accent-red: #e8262a;
    --accent-red-deep: #b51418;
    --ink-dark: #1a1a1a;
    --text-light: #f2f2f2;
  }
  * { box-sizing: border-box; margin: 0; padding: 0; }
  html, body {
    width: 1200px;
    height: 800px;
    overflow: hidden;
    background: var(--page-bg);
  }
  .canvas {
    position: relative;
    width: 1200px;
    height: 800px;
  }

  /* ---------- Information side (horizontal) ---------- */
  .card-info {
    position: absolute;
    left: 60px;
    top: 235px;
    width: 580px;
    height: 330px;
    background: var(--card-dark);
    box-shadow: 0 18px 40px rgba(0,0,0,0.55);
  }
  .org-block {
    position: absolute;
    left: 200px;
    top: 38px;
    color: var(--text-light);
    font-family: "Francois One", "Arial Narrow", sans-serif;
  }
  .org-name {
    font-size: 21px;
    letter-spacing: 0.3px;
    line-height: 1.2;
  }
  .org-motto {
    font-size: 21px;
    line-height: 1.2;
  }
  .name-bar {
    position: absolute;
    left: 36px;
    top: 118px;
    width: 330px;
    height: 32px;
    border-radius: 4px;
    background: linear-gradient(180deg, var(--accent-red) 0%, var(--accent-red-deep) 100%);
    box-shadow: inset 0 0 6px rgba(0,0,0,0.35);
  }
  .employee-name {
    position: absolute;
    left: 52px;
    top: 121px;
    font-family: "Exo 2", sans-serif;
    font-size: 19px;
    letter-spacing: 3px;
    text-transform: uppercase;
    color: var(--ink-dark);
    line-height: 26px;
  }
  .designation {
    position: absolute;
    left: 246px;
    top: 123px;
    font-family: "Exo 2", sans-serif;
    font-size: 15px;
    letter-spacing: 1.5px;
    color: var(--paper-white);
    line-height: 22px;
  }
  .contact-list {
    position: absolute;
    left: 46px;
    top: 180px;
    list-style: none;
    font-family: "Exo 2", sans-serif;
    font-size: 11px;
    letter-spacing: 2.5px;
    text-transform: uppercase;
    color: var(--text-light);
  }
  .contact-item {
    display: flex;
    align-items: center;
    gap: 12px;
    height: 24px;
  }
  .contact-icon {
    width: 13px;
    height: 13px;
    fill: var(--text-light);
    flex: none;
  }

  /* ---------- Image side (vertical) ---------- */
  .card-front {
    position: absolute;
    left: 760px;
    top: 120px;
    width: 330px;
    height: 560px;
    background: var(--card-black);
    overflow: hidden;
    box-shadow: 0 18px 40px rgba(0,0,0,0.55);
  }
  .front-band {
    position: absolute;
    left: 40px;
    top: 0;
    width: 170px;
    height: 100%;
    background: var(--paper-white);
  }
  .brand-mark {
    position: absolute;
    left: 45px;
    top: 190px;
    width: 160px;
    height: 160px;
    border-radius: 50%;
    background: var(--accent-red);
  }
  .brand-name {
    position: absolute;
    left: 40px;
    top: 372px;
    width: 170px;
    text-align: center;
    font-family: "Francois One", "Arial Narrow", sans-serif;
    font-size: 22px;
    color: var(--ink-dark);
  }
</style>
</head>
<body>
<main class="canvas">

  <section class="card-info" aria-label="Business card, information side">
    <div class="org-block">
      <p class="org-name">Calm to Bloom Community Center</p>
      <p class="org-motto">Business Motto</p>
    </div>

    <div class="name-bar"></div>
    <p class="employee-name">Employ Name</p>
    <p class="designation">Designation</p>

    <ul class="contact-list">
      <li class="contact-item">
        <svg class="contact-icon" viewBox="0 0 16 16" aria-hidden="true"><path d="M8 0a5 5 0 0 0-5 5c0 4 5 11 5 11s5-7 5-11a5 5 0 0 0-5-5zm0 7a2 2 0 1 1 0-4 2 2 0 0 1 0 4z"/></svg>
        <span>Address</span>
      </li>
      <li class="contact-item">
        <svg class="contact-icon" viewBox="0 0 16 16" aria-hidden="true"><circle cx="8" cy="8" r="7" fill="none" stroke="#f2f2f2" stroke-width="1.4"/><ellipse cx="8" cy="8" rx="3" ry="7" fill="none" stroke="#f2f2f2" stroke-width="1.2"/><path d="M1 8h14" stroke="#f2f2f2" stroke-width="1.2"/></svg>
        <span>Website</span>
      </li>
      <li class="contact-item">
        <svg class="contact-icon" viewBox="0 0 16 16" aria-hidden="true"><rect x="1" y="1" width="14" height="14" rx="3"/><path d="M5 4l2 2-1 1.2c.6 1.3 1.5 2.2 2.8 2.8L10 9l2 2-1.3 1.3C7 12 4 9 3.7 5.3z" fill="#2c2c2c"/></svg>
        <span>000-000-0000</span>
      </li>
      <li class="contact-item">
        <svg class="contact-icon" viewBox="0 0 16 16" aria-hidden="true"><rect x="0.5" y="3" width="15" height="10" rx="1"/><path d="M1 4l7 5 7-5" fill="none" stroke="#2c2c2c" stroke-width="1.3"/></svg>
        <span>Email@</span>
      </li>
      <li class="contact-item">
        <svg class="contact-icon" viewBox="0 0 16 16" aria-hidden="true"><circle cx="3" cy="13" r="2"/><path d="M1 7a8 8 0 0 1 8 8" fill="none" stroke="#f2f2f2" stroke-width="1.8"/><path d="M1 2a13 13 0 0 1 13 13" fill="none" stroke="#f2f2f2" stroke-width="1.8"/></svg>
        <span>Blog</span>
      </li>
    </ul>
  </section>

  <section class="card-front" aria-label="Business card, image side">
    <div class="front-band"></div>
    <div class="brand-mark"></div>
    <p class="brand-name">Calm to Bloom</p>
  </section>

</main>
</body>
</html>
```